Startup internet service provider needs a good facebook ad

Looking for a catchy facebook ad to launch our internet service in Parker, Colorado. Short video or slideshow preferred, still pictures are okay.

https://www.facebook.com/BrimfoxNetworks

www.brimfox-networks.example

Target Market(s)

Parker Colorado

Colors
add136
0255a3

```html
<!DOCTYPE html>
<html lang="en">
<head>
<meta charset="utf-8">
<title>Brimfox Networks — Fast and Reliable Internet</title>
<link href="https://fonts.googleapis.com/css2?family=Plus+Jakarta+Sans:wght@700;800&family=Inter:wght@300;400&display=swap" rel="stylesheet">
<style>
  :root {
    --brand-blue: #0255a3;
    --deep-blue: #0a3f9c;
    --navy: #062c6e;
    --lime: #add136;
    --ink: #0b2350;
    --white: #ffffff;
    --logo-blue: #14407e;
  }
  html, body {
    margin: 0;
    width: 1200px;
    height: 1000px;
    overflow: hidden;
    background: var(--white);
  }
  .ad {
    position: absolute;
    left: 43px;
    top: 209px;
    width: 1115px;
    height: 583px;
    overflow: hidden;
    background: linear-gradient(100deg, var(--deep-blue) 0%, #1552b8 40%, var(--brand-blue) 70%, var(--navy) 100%);
    font-family: "Plus Jakarta Sans", "Inter", sans-serif;
    color: var(--white);
  }
  .ad__backdrop {
    position: absolute;
    inset: 0;
  }
  .ad__photo {
    position: absolute;
    inset: 0;
    width: 1115px;
    height: 583px;
  }
  .brand {
    position: absolute;
    left: 722px;
    top: 38px;
    display: flex;
    align-items: center;
    gap: 10px;
  }
  .brand__dot {
    width: 36px;
    height: 36px;
    border-radius: 50%;
    background: var(--lime);
  }
  .brand__name {
    font-family: "Plus Jakarta Sans", sans-serif;
    font-weight: 700;
    font-size: 25px;
    color: var(--logo-blue);
  }
  .headline {
    position: absolute;
    left: 75px;
    top: 100px;
    margin: 0;
    font-weight: 800;
    font-size: 60px;
    line-height: 65px;
    letter-spacing: -0.5px;
  }
  .subhead {
    position: absolute;
    left: 75px;
    top: 250px;
    margin: 0;
    font-weight: 800;
    font-size: 31px;
    line-height: 45px;
    letter-spacing: -0.3px;
  }
  .cta {
    position: absolute;
    left: 74px;
    top: 413px;
    width: 192px;
    height: 63px;
    border-radius: 32px;
    background: var(--lime);
    color: var(--ink);
    font-weight: 800;
    font-size: 15.5px;
    display: flex;
    align-items: center;
    justify-content: center;
    box-shadow: 0 0 24px rgba(173, 209, 54, 0.45);
  }
  .contact {
    position: absolute;
    top: 515px;
    display: flex;
    align-items: center;
    gap: 14px;
    font-family: "Inter", sans-serif;
    font-weight: 300;
    font-size: 22px;
  }
  .contact--phone { left: 87px; }
  .contact--email { left: 354px; }
  .contact svg { display: block; }
</style>
</head>
<body>
  <section class="ad">
    <svg class="ad__photo" viewBox="0 0 1115 583" role="img" aria-label="Photograph of a smiling mother and son on a sofa using a tablet in a bright living room with white bookshelves; a blurred, blue-tinted version of the family scene fills the background">
      <defs>
        <linearGradient id="photoTone" x1="0" y1="0" x2="1" y2="1">
          <stop offset="0" stop-color="#eef0f1"/>
          <stop offset="0.45" stop-color="#d9d6d2"/>
          <stop offset="0.75" stop-color="#cdb9ae"/>
          <stop offset="1" stop-color="#b9c4cf"/>
        </linearGradient>
        <radialGradient id="backdropGlow" cx="0.35" cy="0.55" r="0.6">
          <stop offset="0" stop-color="#2a63c4" stop-opacity="0.55"/>
          <stop offset="1" stop-color="#0a3f9c" stop-opacity="0"/>
        </radialGradient>
      </defs>
      <rect width="1115" height="583" fill="url(#backdropGlow)"/>
      <polygon points="392,0 1115,0 1115,448 692,448" fill="url(#photoTone)"/>
      <polygon points="392,0 420,0 720,448 692,448" fill="#5f8fd9" opacity="0.55"/>
      <rect x="692" y="432" width="423" height="16" fill="#8fb1e6" opacity="0.5"/>
    </svg>

    <div class="brand">
      <span class="brand__dot"></span>
      <span class="brand__name">Brimfox Networks</span>
    </div>

    <h1 class="headline">Fast and<br>Reliable</h1>
    <p class="subhead">internet service designed<br>and catered to meet<br>your needs</p>

    <div class="cta">ORDER SERVICE</div>

    <div class="contact contact--phone">
      <svg width="24" height="24" viewBox="0 0 24 24" aria-hidden="true">
        <path fill="#add136" d="M6.6 10.8a15.1 15.1 0 0 0 6.6 6.6l2.2-2.2a1 1 0 0 1 1-.25 11.4 11.4 0 0 0 3.6.57 1 1 0 0 1 1 1V20a1 1 0 0 1-1 1A17 17 0 0 1 3 4a1 1 0 0 1 1-1h3.5a1 1 0 0 1 1 1c0 1.25.2 2.45.57 3.57a1 1 0 0 1-.25 1z"/>
      </svg>
      <span>844-555-0147</span>
    </div>

    <div class="contact contact--email">
      <svg width="26" height="20" viewBox="0 0 26 20" aria-hidden="true">
        <rect x="0" y="0" width="26" height="20" rx="1.5" fill="#add136"/>
        <path d="M1 1.5 13 11 25 1.5" fill="none" stroke="#0a3f9c" stroke-width="1.8"/>
      </svg>
      <span>information@brimfox-networks.example</span>
    </div>
  </section>
</body>
</html>
```